FR / EN Beekeeper research design packaging / label; Beekeeper looking for a design package

I need as a beekeeper to create a design to better showcase my honey. Indeed I work in a natural environment of high quality on a hill called "Veldmoor" (many flowers different fields, few pesticides, ...). I practice a beekeeping respectful of the bee and in a traditional way. I produce a high quality honey (luxury product) for a wealthy clientele looking for good health products, ... The main label should contain only the following text (accompanied by an image): The Veldmoor Honey A variant would also be useful for my production of mead (alcohol from the fermentation of honey): The Veldmoor mead In terms of form, given the target audience, I thought I was moving towards a modern label against a background black and with golden patterns. An example is the honey of the wonders attached, we find a honey assimilated as a real luxury product. Same in the Cuvée Lando Perrusi attachment. I would like to move towards these tones of colors by adding a touch more "champêtre" as on the label of the bottle of wine below where one sees golden flowers drawn, of light and subtle way. Another example that I like is that of the bee of ree joined. Another modern idea identified on this site is this design: https://www.artpitchhub.com/design/30418822 https: //www.artpitchhub. com / design / 30418957 I would also need a round label to place on the lid of the pot with indications of signs (my address) as well as additional information about my product: - BALDUCCI Armand - Veldmoor, 14 - 6812 Hautvelin - 500 g - Spring harvest - Honey all flowers - Flora: rapeseed, fruit trees, clovers - Flavors: sweet honey with vegetal notes Remarks: this is my first artpitchhub project, if you are surprised by some points of the brief or it is missing important information do not hesitate to let me know! ************************************************** ******************************* ENGLISH ****************** ************** I need to beekeeper a new design Indeed, I work in a very natural environment, a high quality eco-system which is the south of Belgium (many different flowers in the fields, few pesticides, ...). I practice a natural beekeeping, in an artisanal way I produce a high quality honey (luxuous product) for wealthy people who are looking for good and healthy products. The following description: The Veldmoor Honey A slight variation could be useful for my production (alcohol from honey fermentation): The Veldmoor Meads Concerning the form, a modern design with golden patterns on a black background could be appropriate. An example is the honey of the wonders in attachment, we could see that honey in this case is a branded like a very luxuous product. I wish to go for these last colors with a more "rural touch" as attachment. We can see golden flowers in a light and elegant manner. Another interesting example is the honey bee in attachment. Some example found on this site: https://www.artpitchhub.com/design/30418822 https: //www.artpitchhub. com / design / 30418957 Balducci Armand - Veldmoor, 14 - 6812 Hautvelin - 500 g - Spring Harvest - Honey all flowers - Flora: rapeseed, fruit, clovers - Flavors: sweet honey with vegetal notes

Target Market(s)

affluent clientele looking for natural products, good for health, ...

Industry/Entity Type

Agriculture

Font styles to use
Decorative
Script
Other font styles liked:
• à la libre appréciation du designer, tant que c'est moderne et élégant

Requirements
Must have
• All text must be in French / A main label and a round label on the lid of the jar. Gilding (preferably on a black background). An image accompanying the text. Gold on a black background
Nice to have
• Elegant and modern design Elegant and modern design
Should not have
• Do not load too much the main label, it must remain uncluttered

```html
<!DOCTYPE html>
<html lang="fr">
<head>
<meta charset="utf-8">
<title>Le Miel du Veldmoor — étiquettes</title>
<link href="https://fonts.googleapis.com/css2?family=Josefin+Sans:wght@300;400&display=swap" rel="stylesheet">
<style>
  :root {
    --paper: #ffffff;
    --black: #0c0c0c;
    --gold: #c8902e;
    --gold-light: #e9b949;
    --gold-deep: #8a5e18;
    --ivory: #f2efe8;
  }
  * { margin: 0; padding: 0; box-sizing: border-box; }
  html, body { width: 1200px; height: 839px; overflow: hidden; background: var(--paper); }
  body { position: relative; font-family: "Josefin Sans", sans-serif; font-weight: 300; }

  /* Lid label */
  .lid-label { position: absolute; left: 92px; top: 220px; width: 472px; height: 472px; }
  .lid-label svg { position: absolute; inset: 0; }
  .lid-label .line {
    position: absolute; left: 0; width: 472px; text-align: center; white-space: nowrap;
  }
  .gold { color: var(--gold); }
  .ivory { color: var(--ivory); }
  .lid-bee { position: absolute; left: 206px; top: 66px; width: 60px; height: 36px;
             background: radial-gradient(ellipse, var(--gold-light), var(--gold-deep) 70%, transparent 72%); }
  .lid-rule { position: absolute; left: 178px; top: 194px; width: 118px; height: 5px;
              background: linear-gradient(90deg, var(--gold-light), var(--gold)); }
  .lid-title { font-size: 35px; letter-spacing: 0.5px; }

  /* Main jar label */
  .main-label { position: absolute; left: 612px; top: 268px; width: 490px; height: 468px;
                background: var(--black); overflow: hidden; }
  .main-border { position: absolute; left: 0; top: 20px; width: 100%; height: 20px;
                 background: linear-gradient(90deg, var(--gold-deep), var(--gold-light), var(--gold), var(--gold-light), var(--gold-deep)); }
  .main-border::after { content: ""; position: absolute; left: 0; right: 0; bottom: -5px; height: 1px; background: var(--gold); }
  .harvest { position: absolute; left: 32px; top: 86px; font-size: 11.5px; line-height: 15px; color: var(--ivory); }
  .harvest .flora { color: var(--gold); font-size: 10px; }
  .main-bee { position: absolute; left: 214px; top: 150px; width: 62px; height: 40px;
              background: radial-gradient(ellipse, var(--gold-light), var(--gold-deep) 70%, transparent 72%); }
  .brand { position: absolute; left: 0; width: 100%; text-align: center; font-size: 42px; white-space: nowrap; }
  .brand.top { top: 210px; color: var(--gold); }
  .brand.bottom { top: 258px; color: var(--ivory); }
  .weight { position: absolute; left: 0; width: 100%; top: 318px; text-align: center; font-size: 14px; color: var(--gold); }
  .meadow { position: absolute; left: 0; bottom: 0; width: 100%; height: 132px;
            background: linear-gradient(180deg, rgba(12,12,12,0) 0%, rgba(110,82,28,0.35) 55%, rgba(90,66,22,0.55) 100%); }
</style>
</head>
<body>

  <section class="lid-label" aria-label="Étiquette de couvercle">
    <svg width="472" height="472" viewBox="0 0 472 472">
      <circle cx="236" cy="236" r="236" fill="var(--black)"/>
      <circle cx="236" cy="236" r="222" fill="none" stroke="var(--gold)" stroke-width="14" role="img" aria-label="Frise ornementale dorée en couronne"/>
      <circle cx="236" cy="236" r="208" fill="none" stroke="var(--gold)" stroke-width="1.2"/>
    </svg>
    <div class="lid-bee" role="img" aria-label="Illustration d'abeille dorée"></div>
    <div class="line lid-title gold" style="top:118px">LE MIEL DU</div>
    <div class="line lid-title ivory" style="top:156px">VELDMOOR</div>
    <div class="lid-rule" role="img" aria-label="Frise dorée"></div>
    <div class="line ivory" style="top:226px;font-size:16px">RÉCOLTE DE PRINTEMPS</div>
    <div class="line ivory" style="top:247px;font-size:16px">MIEL TOUTES FLEURS</div>
    <div class="line gold" style="top:284px;font-size:19px">Flore : colza, fruitiers, trêfles</div>
    <div class="line gold" style="top:308px;font-size:17px">Saveurs : miel doux aux notes végétales</div>
    <div class="line ivory" style="top:342px;font-size:15.5px">BALDUCCI Armand, Veldmoor, 14</div>
    <div class="line ivory" style="top:364px;font-size:15.5px">6812 Hautvelin</div>
    <div class="line gold" style="top:393px;font-size:20px">500 g</div>
  </section>

  <section class="main-label" aria-label="Étiquette principale">
    <div class="main-border" role="img" aria-label="Frise ornementale dorée"></div>
    <div class="harvest">
      RÉCOLTE DE PRINTEMPS<br>
      MIEL TOUTES FLEURS<br>
      <span class="flora">Flore : colza, fruitiers, trêfles</span>
    </div>
    <div class="main-bee" role="img" aria-label="Illustration d'abeille dorée"></div>
    <div class="brand top">LE MIEL DU</div>
    <div class="brand bottom">VELDMOOR</div>
    <div class="weight">500 g</div>
    <div class="meadow" role="img" aria-label="Fleurs des champs dorées et abeilles en vol"></div>
  </section>

</body>
</html>
```